Rear Window Advertisement and Magnets for side doors

Questions about Sanovolt insurance?
Ask me, I'm a nurse
472-###-####
(Disclaimer.................in small print....)

```html
<!DOCTYPE html>
<html lang="en">
<head>
<meta charset="utf-8">
<title>Sanovolt Door Magnet</title>
<link href="https://fonts.googleapis.com/css2?family=Gochi+Hand&family=Roboto+Condensed:wght@700&family=Playfair+Display:wght@900&display=swap" rel="stylesheet">
<style>
  :root {
    --stage: #000000;
    --card: #ffffff;
    --rose: #c8659e;
    --rose-band: #d576ab;
    --ink: #231f20;
    --beige: #d6d2c9;
    --white: #ffffff;
  }
  html, body {
    margin: 0;
    padding: 0;
    width: 960px;
    height: 1200px;
    overflow: hidden;
    background: var(--stage);
  }
  .magnet {
    position: absolute;
    left: 80px;
    top: 300px;
    width: 800px;
    height: 600px;
    background: var(--card);
    border-radius: 20px;
    overflow: hidden;
  }
  .headline {
    position: absolute;
    left: 50px;
    top: 28px;
    margin: 0;
    font-family: "Gochi Hand", cursive;
    font-weight: 400;
    font-size: 56px;
    line-height: 54px;
    color: var(--rose);
  }
  .nurse-art {
    position: absolute;
    left: 537px;
    top: 120px;
    width: 280px;
    height: 270px;
    border-radius: 140px 140px 0 0;
    background: var(--beige);
  }
  .bubble {
    position: absolute;
    left: 40px;
    top: 172px;
    width: 560px;
    height: 186px;
  }
  .bubble-text {
    position: absolute;
    left: 100px;
    top: 208px;
    margin: 0;
    font-family: "Roboto Condensed", sans-serif;
    font-weight: 700;
    font-size: 60px;
    line-height: 58px;
    color: var(--white);
  }
  .band {
    position: absolute;
    left: 0;
    top: 390px;
    width: 800px;
    height: 210px;
    background: var(--rose-band);
  }
  .phone {
    position: absolute;
    left: 0;
    width: 800px;
    top: 22px;
    margin: 0;
    text-align: center;
    font-family: "Playfair Display", serif;
    font-weight: 900;
    font-size: 98px;
    line-height: 130px;
    font-variant-numeric: lining-nums;
    letter-spacing: -1px;
    color: var(--white);
  }
  .disclaimer {
    position: absolute;
    left: 57px;
    top: 166px;
    margin: 0;
    font-family: Arial, Helvetica, sans-serif;
    font-style: italic;
    font-size: 15px;
    color: var(--ink);
  }
</style>
</head>
<body>
  <div class="magnet">
    <h1 class="headline">Questions about<br>Sanovolt insurance?</h1>

    <div class="nurse-art" role="img" aria-label="Illustration of a smiling nurse with a stethoscope raising one finger"></div>

    <svg class="bubble" viewBox="0 0 560 186" aria-hidden="true">
      <rect x="4" y="4" width="470" height="178" rx="38" fill="none" stroke="var(--ink)" stroke-width="6"/>
      <path d="M58 22 H430 Q462 22 462 54 V104 L540 90 L458 140 Q448 162 420 162 H58 Q22 162 22 126 V58 Q22 22 58 22 Z" fill="var(--rose)"/>
    </svg>
    <p class="bubble-text">Ask me,<br>I'm a nurse</p>

    <div class="band">
      <p class="phone">472-###-####</p>
      <p class="disclaimer">Disclaimer:</p>
    </div>
  </div>
</body>
</html>
```